Apricot Variety Sheet - Meadowlark Orchard Co

We are needing a variety sheet that we can hand out that will describe the different apricot vatieties we have available. The attached document has the name of the variety along with a description that will need to be on the sheet. We are looking for a modern, appealing way to display this information on 1 page (if needed, it can be front and back)
Updates

Apologies for the delay; we are overwhelmed with the great design options and will be sorting through them all (across our contests) to pick a collective. Thank you for your patience.

Target Market(s)

Growers and consumers

Industry/Entity Type

Agriculture

Requirements
Must have
• Easy to read
• Natural color palettes to emphasize the agricultural nature
• Clearly show washington as the origin in the title or at the top
Nice to have
• incorporate Apricots in the design

```html
<!DOCTYPE html>
<html lang="en">
<head>
<meta charset="utf-8">
<title>Washington State Apricot Variety Sheet – Meadowlark Orchard Co</title>
<link rel="stylesheet" href="https://fonts.googleapis.com/css2?family=Archivo+Black&family=Source+Sans+3:wght@400;700&display=swap">
<style>
  :root {
    --brown: #4a3324;
    --band: #4b3a2c;
    --panel: rgba(28, 112, 40, 0.86);
    --orange: #f07a1e;
    --white: #ffffff;
    --brand-green: #2f9a36;
    --leaf-light: #9ec86a;
    --leaf-dark: #4f7f2e;
    --hill: #8a7150;
    --river: #5f7f95;
    --apricot: #f29a3a;
    --apricot-deep: #d9642a;
  }
  * { margin: 0; padding: 0; box-sizing: border-box; }
  html, body { width: 1200px; height: 927px; overflow: hidden; background: #fff; }
  .sheet {
    position: relative; width: 1200px; height: 927px; overflow: hidden;
    font-family: "Source Sans 3", "Myriad Pro", Arial, sans-serif;
  }
  .header-photo {
    position: absolute; left: 0; top: 0; width: 1200px; height: 156px;
    background: linear-gradient(100deg, #c9dd98 0%, var(--leaf-light) 30%, #b9cf9c 55%, var(--leaf-dark) 80%, #6f9b42 100%);
  }
  .title {
    position: absolute; left: 78px; top: 30px;
    font-family: "Archivo Black", "Arial Black", sans-serif;
    font-size: 38px; line-height: 48px; color: var(--brown); letter-spacing: 0.3px;
  }
  .brand { position: absolute; left: 695px; top: 28px; display: flex; align-items: center; gap: 18px; }
  .brand-mark { width: 110px; height: 110px; border-radius: 50%; background: #e25a3a; flex: none; }
  .brand-name {
    font-family: "Source Sans 3", Arial, sans-serif; font-weight: 700;
    font-size: 30px; line-height: 32px; color: var(--brand-green);
  }
  .band { position: absolute; left: 0; width: 1200px; background: var(--band); }
  .band-top { top: 156px; height: 12px; }
  .band-bottom { top: 808px; height: 14px; }
  .landscape-photo {
    position: absolute; left: 0; top: 168px; width: 1200px; height: 640px;
    background:
      linear-gradient(180deg, #a89270 0%, var(--hill) 18%, var(--river) 26%, #6d6a4a 34%, #3f5a2e 60%, #2f4a24 100%);
  }
  .panel {
    position: absolute; top: 168px; height: 640px; background: var(--panel);
    padding: 25px 22px 0 29px; color: var(--white);
  }
  .panel-left { left: 118px; width: 427px; }
  .panel-right { left: 655px; width: 428px; }
  .variety { font-size: 16.6px; line-height: 21.6px; margin-bottom: 6px; }
  .variety-name {
    color: var(--orange); font-weight: 700; font-variant: small-caps; font-size: 19px;
  }
  .variety-name::before { content: "• "; }
  .apricot-photo {
    position: absolute; left: 0; top: 822px; width: 1200px; height: 105px;
    background: radial-gradient(circle at 10% 50%, var(--apricot) 0%, var(--apricot-deep) 60%),
                linear-gradient(90deg, var(--apricot), var(--apricot-deep));
    background-blend-mode: normal;
  }
  .web {
    position: absolute; left: 0; width: 1200px; top: 870px; text-align: center;
    font-weight: 700; font-size: 24px; color: var(--brand-green);
  }
</style>
</head>
<body>
<div class="sheet">
  <div class="header-photo" role="img" aria-label="Sunlit apricot orchard trees"></div>
  <h1 class="title">WASHINGTON STATE<br>APRICOT VARIETY SHEET</h1>
  <div class="brand">
    <div class="brand-mark"></div>
    <div class="brand-name">Meadowlark<br>Orchard Co</div>
  </div>
  <div class="band band-top"></div>

  <div class="landscape-photo" role="img" aria-label="Aerial view of orchards on hills beside a river"></div>

  <section class="panel panel-left">
    <p class="variety"><span class="variety-name">Rival.</span> Great flavor with a fine, firm texture distinguishes this large oval-shaped apricot. The skin is light orange with a red blush. The flesh is a lush deep orange color. Available early July-early August.</p>
    <p class="variety"><span class="variety-name">Robada.</span> This jumbo apricot has a delicious floral flavor with a firm texture. Bright orange, with a deep red blush over nearly half its surface. Available early June.</p>
    <p class="variety"><span class="variety-name">Perfection.</span> This classic large oval apricot is deep orange with an oblong shape and firm texture. The flesh is a yellow/orange color that is very sweet and full of flavor. Available mid July - mid August.</p>
    <p class="variety"><span class="variety-name">Patterson,</span> This apricot has a well-balanced flavor and an excellent shelf life. This is perfect for canning or drying. It has streaked red over yellow skin, with a firm flesh. Available mid – late June.</p>
    <p class="variety"><span class="variety-name">Tomcot.</span> Tangy, sweet flavor with a firm texture. This oval apricot is light orange with a slight blush color. The flesh is a dark orange. Available late June – late July.</p>
    <p class="variety"><span class="variety-name">Goldrich.</span> This apricot is round with a bright orange skin color and a deep orange flesh. It has a mild, sweet flavor with a firm texture. Available early July – mid August.</p>
  </section>

  <section class="panel panel-right">
    <p class="variety"><span class="variety-name">Casselbrite.</span> This medium sized apricot is golden orange with a slight red blush. It has a mild sweet-tart flavor that is good for eating out of hand. Available late June- early July.</p>
    <p class="variety"><span class="variety-name">Goldbar.</span> Moderately juicy, this large oval-shaped apricot has a light yellow-orange with a reddish blush. The flesh is firm, meaty, and has a light orange color. Available late June – end of July.</p>
    <p class="variety"><span class="variety-name">Sweet Juillet.</span> This special variety has a unique, sweet flavor with a juicy flesh. It is bright orange in color with a bright orange flesh. Available through July.</p>
    <p class="variety"><span class="variety-name">Tasty Rich.</span> This early variety is light yellow-orange colored with a firm texture. Very juicy with an enticing flavor. Available through June.</p>
    <p class="variety"><span class="variety-name">Goldstrike.</span> A larger apricot with light orange, blushed skin. Firm texture with a slight tart taste until fully ripened, then very sweet. Available mid June - mid July.</p>
    <p class="variety"><span class="variety-name">Riland.</span> Very aromatic and sweet, this apricot is orange with a red blush. It has a yellow-orange colored flesh and a round shape. Available mid-June to end of July.</p>
  </section>

  <div class="band band-bottom"></div>
  <div class="apricot-photo" role="img" aria-label="Close-up of piled ripe apricots"></div>
  <p class="web">www.meadowlarkorchard.com</p>
</div>
</body>
</html>
```